Marvolite Graphic for Engerydrink label

We need a graphic design for a new private label energy drink.
called "Marvolite"
We would like to see designs that use the colours ;
red, gray, yellow, and black
The final design should see a Tough face which appeals to young
people

```html
<!DOCTYPE html>
<html lang="en">
<head>
<meta charset="utf-8">
<title>Marvolite energy drink label</title>
<link rel="stylesheet" href="https://fonts.googleapis.com/css2?family=Noto+Serif:wght@800&family=Sniglet:wght@800&display=swap">
<style>
  :root {
    --page-bg: #ffffff;
    --label-light: #ffffff;
    --label-shade: #e3e3e3;
    --label-edge: #a9a9a9;
    --brand-red: #e5100f;
    --scribble-yellow: #f7d417;
    --ink-black: #141414;
    --ink-white: #ffffff;
    --art-dark: #2a2a2a;
    --art-mid: #8a8a8a;
    --art-light: #dcdcdc;
  }
  html, body {
    margin: 0;
    width: 1200px;
    height: 1121px;
    overflow: hidden;
    background: var(--page-bg);
  }
  .canvas {
    position: relative;
    width: 1200px;
    height: 1121px;
  }
  .label {
    position: absolute;
    left: 259px;
    top: 57px;
    width: 682px;
    height: 1006px;
    box-sizing: border-box;
    border: 1.5px solid var(--label-edge);
    border-radius: 7px;
    background: radial-gradient(ellipse at 45% 40%, var(--label-light) 0%, var(--label-light) 45%, var(--label-shade) 100%);
    overflow: hidden;
  }
  .label__art {
    position: absolute;
    inset: 0;
    width: 100%;
    height: 100%;
  }
  .label__brand {
    position: absolute;
    left: 122px;
    top: 651px;
    margin: 0;
    transform-origin: 0 0;
    transform: rotate(-90deg);
    font-family: "Noto Serif", serif;
    font-weight: 800;
    font-size: 118px;
    line-height: 1;
    letter-spacing: -5px;
    color: var(--brand-red);
    white-space: nowrap;
  }
  .label__tagline {
    position: absolute;
    left: 397px;
    top: 795px;
    margin: 0;
    transform: translate(-50%, -50%) rotate(-31deg);
    font-family: "Sniglet", sans-serif;
    font-weight: 800;
    font-size: 66px;
    line-height: 1;
    color: var(--ink-black);
    white-space: nowrap;
    -webkit-text-stroke: 1px var(--ink-black);
    text-shadow:
      -3px -3px 0 var(--ink-white), 3px -3px 0 var(--ink-white),
      -3px 3px 0 var(--ink-white), 3px 3px 0 var(--ink-white),
      6px 6px 0 var(--ink-black);
  }
</style>
</head>
<body>
<main class="canvas">
  <section class="label">
    <svg class="label__art" viewBox="0 0 682 1006" xmlns="http://www.w3.org/2000/svg">
      <defs>
        <linearGradient id="art-tone" x1="0" y1="0" x2="1" y2="1">
          <stop offset="0" stop-color="var(--art-dark)"/>
          <stop offset="0.55" stop-color="var(--art-mid)"/>
          <stop offset="1" stop-color="var(--art-light)"/>
        </linearGradient>
      </defs>
      <path class="label__scribble" role="img" aria-label="Yellow crayon scribble behind the tagline"
            fill="var(--scribble-yellow)" opacity="0.85"
            d="M140 900 C150 820 300 720 420 660 C500 620 600 600 625 640 C640 700 560 780 470 840 C380 900 250 985 170 970 C135 960 132 930 140 900 Z"/>
      <rect class="label__illustration" role="img" aria-label="Illustration of a tough masked face in black, grey and red"
            x="250" y="90" width="335" height="585" rx="12" fill="url(#art-tone)"/>
    </svg>
    <h1 class="label__brand">Marvolite</h1>
    <p class="label__tagline">energy drink.</p>
  </section>
</main>
</body>
</html>
```